Silver Heron Holdings, LLC Business Card

We need a logo that will be embossed or printed in a singular light color for Business Cards. Would be interested in seeing a Cypress Tree graphic. Our company name is Silver Heron Holdings, LLC. Business Card layout and graphic should project imagine of confidence, integrity and strength.

```html
<!DOCTYPE html>
<html lang="en">
<head>
<meta charset="utf-8">
<title>Silver Heron Holdings, LLC — Business Card</title>
<link rel="stylesheet" href="https://fonts.googleapis.com/css2?family=Cinzel:wght@400&family=Open+Sans:wght@400;600&display=swap">
<style>
  :root {
    --ink: #000000;
    --paper: #ffffff;
    --silver: #a9a9a9;
    --backdrop: #e6ddc8;
    --text-dark: #1a1a1a;
    --tagline: #dcdcdc;
  }
  * { box-sizing: border-box; margin: 0; padding: 0; }
  html, body { width: 1200px; height: 800px; overflow: hidden; }
  body {
    background: var(--backdrop);
    position: relative;
    font-family: "Open Sans", Arial, sans-serif;
  }
  .card {
    position: absolute;
    top: 240px;
    width: 530px;
    height: 310px;
    border-radius: 40px;
    overflow: hidden;
  }

  /* Back of card */
  .card-back { left: 45px; background: var(--ink); }
  .card-back .tree-mark {
    position: absolute;
    left: 180px; top: 35px;
    width: 170px; height: 135px;
    background: var(--silver);
    border-radius: 50% 50% 40% 40% / 60% 60% 40% 40%;
  }
  .card-back .tagline {
    position: absolute;
    top: 180px; left: 0; right: 0;
    text-align: center;
    font-family: "Cinzel", "Times New Roman", serif;
    font-size: 11px;
    letter-spacing: 0.5px;
    color: var(--tagline);
  }
  .card-back .web-tag {
    position: absolute;
    left: 200px; top: 272px;
    width: 150px; height: 20px;
    background: var(--paper);
    color: var(--text-dark);
    font-size: 8.5px;
    font-weight: 600;
    line-height: 20px;
    text-align: center;
  }

  /* Front of card */
  .card-front { left: 625px; background: var(--paper); }
  .card-front .company-name {
    position: absolute;
    top: 16px; left: 0; right: 0;
    text-align: center;
    font-family: "Cinzel", "Times New Roman", serif;
    font-weight: 400;
    font-size: 29px;
    color: var(--ink);
    letter-spacing: 0.5px;
    white-space: nowrap;
  }
  .card-front .rule-thick,
  .card-front .rule-thin {
    position: absolute; left: 0; right: 0;
    background: var(--ink);
  }
  .card-front .rule-thick { top: 60px; height: 5px; }
  .card-front .rule-thin { top: 70px; height: 2px; }
  .card-front .base-band {
    position: absolute;
    left: 0; right: 0; bottom: 0;
    height: 78px;
    background: var(--ink);
  }
  .card-front .tree-mark {
    position: absolute;
    left: 45px; top: 100px;
    width: 170px; height: 135px;
    background: var(--ink);
    border-radius: 50% 50% 40% 40% / 60% 60% 40% 40%;
  }
  .card-front .divider {
    position: absolute;
    left: 270px; top: 112px;
    width: 1.5px; height: 100px;
    background: var(--ink);
  }
  .contact-list {
    position: absolute;
    left: 280px; top: 112px;
    list-style: none;
    font-size: 12px;
    color: var(--text-dark);
  }
  .contact-list li {
    display: flex; align-items: center;
    height: 20px; gap: 6px;
    white-space: nowrap;
  }
  .contact-list svg { width: 11px; height: 11px; flex: none; }
  .contact-list .dot {
    width: 10px; height: 10px; flex: none;
    background: var(--ink);
  }
  .contact-list .dot.round { border-radius: 50%; }
</style>
</head>
<body>

  <section class="card card-back" aria-label="Card back">
    <div class="tree-mark" role="img" aria-label="Broad tree silhouette in light grey"></div>
    <p class="tagline">Rooted in Strength and Trust</p>
    <p class="web-tag">www.silverheronholdings.com</p>
  </section>

  <section class="card card-front" aria-label="Card front">
    <h1 class="company-name">Silver Heron Holdings, LLC</h1>
    <div class="rule-thick"></div>
    <div class="rule-thin"></div>
    <div class="tree-mark" role="img" aria-label="Broad tree silhouette in dark ink"></div>
    <div class="base-band"></div>
    <div class="divider"></div>
    <ul class="contact-list">
      <li>
        <svg viewBox="0 0 12 12" aria-hidden="true"><path d="M2 1 L4.5 1 L5.5 3.8 L4 5 Q5 7.2 7 8 L8.2 6.5 L11 7.5 L11 10 Q11 11 10 11 Q1 10.5 1 2 Q1 1 2 1 Z" fill="#000"/></svg>
        <span>555-014-2290</span>
      </li>
      <li>
        <svg viewBox="0 0 12 12" aria-hidden="true"><rect x="0.8" y="2.3" width="10.4" height="7.4" fill="none" stroke="#000" stroke-width="1.2"/><path d="M1 2.5 L6 6.5 L11 2.5" fill="none" stroke="#000" stroke-width="1.2"/></svg>
        <span>info@silverheronholdings.com</span>
      </li>
      <li>
        <span class="dot"></span>
        <span>SilverHeronHoldingsGroup</span>
      </li>
      <li>
        <span class="dot round"></span>
        <span>@Silver_Heron</span>
      </li>
    </ul>
  </section>

</body>
</html>
```